Fundmoor campaign

Edit a fundmoor web page already made.
I will give you access to the site, I don't see coding nessecary.
https://www.fundmoor-example.com/projects/lumensnap/swift-steady-camera-mount-swift-small-and-steady?ref=qelturx&token=3e9d17c4

Target Market(s)

Photographers

Industry/Entity Type

Photography

```html
<!DOCTYPE html>
<html lang="en">
<head>
<meta charset="utf-8">
<title>Swift Steady Camera Mount – Fundmoor</title>
<link rel="stylesheet" href="https://fonts.googleapis.com/css2?family=Inter:wght@400;500&display=swap">
<style>
  :root {
    --page-bg: #f9f9f7;
    --ink: #1f1f1f;
    --ink-soft: #4a4a4a;
    --ink-muted: #5e5e5e;
    --rule: #e4e4e2;
    --accent: #117a48;
    --play: #0f6652;
    --box-bg: #efefed;
    --box-line: #dcdcda;
    --icon: #3f3f3f;
  }
  * { margin: 0; padding: 0; box-sizing: border-box; }
  html, body { width: 1200px; height: 521px; overflow: hidden; }
  body {
    position: relative;
    background: var(--page-bg);
    font-family: "Inter", sans-serif;
    color: var(--ink);
  }
  .campaign-title {
    position: absolute; top: 18px; left: 0; width: 100%;
    text-align: center; font-size: 20.5px; font-weight: 400; letter-spacing: 0.2px;
  }
  .campaign-subtitle {
    position: absolute; top: 51px; left: 0; width: 100%;
    text-align: center; font-size: 15.5px; font-weight: 400; color: var(--ink);
  }
  .campaign-video {
    position: absolute; left: 45px; top: 111px; width: 744px; height: 410px;
    background: linear-gradient(90deg, #050505 0%, #0d0d0d 40%, #1a1613 62%, #8a6a58 78%, #b48a73 88%, #2a2522 100%);
    overflow: hidden;
  }
  .video-wordmark {
    position: absolute; left: 78px; top: 300px;
    font-size: 20px; line-height: 25px; font-weight: 500; color: #9a9a9a; letter-spacing: 1px;
  }
  .play-button {
    position: absolute; left: 316px; top: 178px; width: 111px; height: 62px;
    background: var(--play); border: 2px solid #fff;
    display: flex; align-items: center; justify-content: center;
  }
  .funding-panel { position: absolute; left: 821px; top: 111px; width: 356px; }
  .progress-track { height: 5px; background: var(--rule); }
  .stat-amount { margin-top: 22px; font-size: 24px; line-height: 26px; }
  .stat-number { font-size: 22px; line-height: 24px; color: var(--ink-soft); }
  .stat-label { font-size: 13px; line-height: 16px; color: var(--ink-muted); margin-top: 4px; }
  .stat-backers { margin-top: 26px; }
  .stat-days { margin-top: 23px; }
  .back-button {
    margin-top: 18px; height: 42px; background: var(--accent); color: #fff;
    display: flex; align-items: center; justify-content: center; font-size: 15.5px;
  }
  .share-row { margin-top: 16px; display: flex; align-items: center; height: 37px; }
  .remind-button {
    width: 178px; height: 37px; border: 1px solid #cfcfcd; background: #fff;
    display: flex; align-items: center; justify-content: center; gap: 12px; font-size: 13.5px;
  }
  .share-icons { display: flex; gap: 22px; margin-left: auto; align-items: center; }
  .share-icons svg { display: block; }
  .status-box {
    margin-top: 17px; height: 70px; background: var(--box-bg);
    border: 1px solid var(--box-line); padding: 17px 17px 0;
  }
  .status-title { font-size: 16px; line-height: 20px; }
  .status-text { font-size: 12.5px; line-height: 16px; margin-top: 9px; color: var(--ink); }
</style>
</head>
<body>
  <h1 class="campaign-title">Swift Steady Camera Mount: Swift, small and steady</h1>
  <p class="campaign-subtitle">Our new versatile tripod head allows for individual adjustments to make framing and set-up quicker and easier</p>

  <div class="campaign-video" role="img" aria-label="Video still: a hand holding a compact camera mounted on the black tripod head with a looped metal clamp">
    <div class="video-wordmark">SWIFT<br>STEADY<br>MOUNT</div>
    <div class="play-button">
      <svg width="14" height="16" viewBox="0 0 14 16"><path d="M1 1 L13 8 L1 15 Z" fill="#fff"/></svg>
    </div>
  </div>

  <aside class="funding-panel">
    <div class="progress-track"></div>
    <div class="stat-amount">NOK 0</div>
    <div class="stat-label">pledged of NOK 64,000 goal</div>
    <div class="stat-backers">
      <div class="stat-number">0</div>
      <div class="stat-label">backers</div>
    </div>
    <div class="stat-days">
      <div class="stat-number">30</div>
      <div class="stat-label">days to go</div>
    </div>
    <div class="back-button">Back this project</div>
    <div class="share-row">
      <div class="remind-button">
        <svg width="11" height="13" viewBox="0 0 11 13"><path d="M1 1 H10 V12 L5.5 8.5 L1 12 Z" fill="none" stroke="#1f1f1f" stroke-width="1.5"/></svg>
        <span>Remind me</span>
      </div>
      <div class="share-icons">
        <svg width="16" height="16" viewBox="0 0 16 16" aria-label="Share"><circle cx="8" cy="8" r="7.5" fill="#3b5bb5"/></svg>
        <svg width="16" height="16" viewBox="0 0 16 16" aria-label="Share"><circle cx="8" cy="8" r="7.5" fill="#2aa0e8"/></svg>
        <svg width="17" height="12" viewBox="0 0 17 12" aria-label="Email"><rect x="0.75" y="0.75" width="15.5" height="10.5" fill="none" stroke="var(--icon)" stroke-width="1.5"/><path d="M1 1 L8.5 7 L16 1 M1 11 L6.5 5.5 M16 11 L10.5 5.5" fill="none" stroke="var(--icon)" stroke-width="1.3"/></svg>
        <svg width="18" height="13" viewBox="0 0 18 13" aria-label="Embed"><path d="M5 2 L1 6.5 L5 11 M13 2 L17 6.5 L13 11 M10.5 1 L7.5 12" fill="none" stroke="var(--icon)" stroke-width="1.4"/></svg>
      </div>
    </div>
    <div class="status-box">
      <div class="status-title">This project is not live</div>
      <div class="status-text">This is only a draft that the creator has chosen to</div>
    </div>
  </aside>
</body>
</html>
```